Hop Grower Producer Card

A wisconsin based grower of high quality mid westrn grown Hops with the concept of growing and processing Hops into pellet form for sale to brewers of beer large and small .varieties are grown are Cascade ,Chinook and Centennial

Target Market(s)

Brew masters at micro brews and large breweries

Industry/Entity Type

Processing

Font styles to use
Decorative
Script

Requirements
Must have
• i would like the Hop varieties listed on the back of the card , with the statement Grower of High Quality Wisconsin Hops and the web site address
Nice to have
• german style font for the name Velmar's Bine Hollow

```html
<!DOCTYPE html>
<html lang="en">
<head>
<meta charset="utf-8">
<title>Velmar's Bine Hollow – Business Card</title>
<link href="https://fonts.googleapis.com/css2?family=UnifrakturMaguntia&family=Italianno&family=Marcellus&family=Varela+Round&display=swap" rel="stylesheet">
<style>
  :root {
    --stage: #8a6a4a;
    --front-dark: #050505;
    --front-green: #2f4a1e;
    --title-tan: #ebb47e;
    --tagline-orange: #d7852c;
    --leaf-green: #7cc242;
    --soft-grey: #a8b4a6;
    --rule-green: #7cc242;
    --back-white: #ffffff;
    --ink-black: #0b0b0b;
    --back-green: #3c8a3c;
    --back-deep: #1f5a26;
  }
  * { box-sizing: border-box; margin: 0; padding: 0; }
  html, body { width: 900px; height: 1200px; overflow: hidden; }
  body { background: var(--stage); position: relative; font-family: "Marcellus", serif; }

  .card { position: absolute; left: 25px; width: 848px; height: 495px; overflow: hidden;
          box-shadow: 0 4px 14px rgba(0,0,0,.35); }
  .card--front { top: 84px;
    background: linear-gradient(100deg, var(--front-dark) 55%, var(--front-green) 100%); }
  .card--back { top: 622px; background: var(--back-white); }

  .brand-name { position: absolute; left: 0; right: 0; text-align: center;
    font-family: "UnifrakturMaguntia", serif; line-height: 1; }
  .card--front .brand-name { top: 38px; font-size: 66px; color: var(--title-tan); letter-spacing: 1px; }
  .card--back .brand-name { top: 44px; font-size: 72px; color: var(--ink-black); letter-spacing: 1px; }

  .tagline { position: absolute; left: 0; right: 0; text-align: center; }
  .card--front .tagline { top: 125px; font-family: "Varela Round", sans-serif; font-size: 33px;
    color: var(--tagline-orange); }
  .card--back .tagline { top: 135px; font-size: 30px; color: var(--back-green); font-weight: 700; }

  .beer-photo { position: absolute; left: 0; top: 190px; width: 520px; height: 305px;
    background:
      radial-gradient(ellipse 120px 110px at 250px 140px, rgba(255,232,90,.95), rgba(240,190,40,.5) 45%, transparent 75%),
      radial-gradient(ellipse 70px 110px at 110px 185px, #c2621a, #8a3a0c 70%, transparent 100%),
      radial-gradient(ellipse 60px 40px at 400px 220px, #9bc24a, #5a7f22 70%, transparent 100%),
      linear-gradient(180deg, transparent 70%, #2a1608 100%); }

  .contact { position: absolute; right: 42px; top: 196px; width: 262px; text-align: right;
    color: var(--leaf-green); font-size: 19px; line-height: 1.32; }
  .contact .person { font-family: "Italianno", cursive; font-size: 46px; line-height: 1; }
  .contact .role { color: var(--soft-grey); font-size: 20px; margin-bottom: 8px; }
  .contact .rule { height: 1px; background: var(--rule-green); margin: 0 0 6px; }
  .contact .block { margin-bottom: 6px; }

  .hop-photo { position: absolute; left: 0; top: 180px; width: 848px; height: 315px;
    background:
      radial-gradient(ellipse 320px 170px at 300px 250px, rgba(150,190,80,.9), rgba(120,160,70,.55) 55%, transparent 85%),
      radial-gradient(ellipse 180px 120px at 80px 140px, rgba(60,110,40,.8), transparent 80%),
      linear-gradient(180deg, rgba(255,255,255,0) 0%, rgba(190,210,170,.6) 60%, rgba(110,150,80,.75) 100%); }
  .varieties { position: absolute; left: 0; right: 0; top: 186px; text-align: center;
    font-size: 28px; color: var(--back-deep); }
  .web { position: absolute; left: 0; right: 0; top: 230px; text-align: center;
    font-size: 24px; color: var(--back-deep); font-weight: 700; }
</style>
</head>
<body>
  <section class="card card--front">
    <h1 class="brand-name">Velmar's Bine Hollow</h1>
    <p class="tagline">Grower Of High Quality Wisconsin Hops</p>
    <div class="beer-photo" role="img" aria-label="Two glasses of amber beer with hop cones and wheat on a table, glowing light behind"></div>
    <div class="contact">
      <p class="person">Otto Velmar</p>
      <p class="role">Owner /Manager</p>
      <div class="rule"></div>
      <p class="block">1240 Millbrook Lane<br>Redgranite, WI 54970</p>
      <p class="block">Cell : 715-555-0142<br>Fax : 715-555-0187</p>
      <div class="rule"></div>
      <p>binehollow21@mailbox.com<br>www.binehollow21.com</p>
    </div>
  </section>

  <section class="card card--back">
    <div class="hop-photo" role="img" aria-label="Green hop cones hanging from a leafy bine against a soft blurred field"></div>
    <h2 class="brand-name">Velmar's Bine Hollow</h2>
    <p class="tagline">Grower Of High Quality Wisconsin Hops</p>
    <p class="varieties">Cascade, Chinook, Centennial</p>
    <p class="web">www.binehollow21.com</p>
  </section>
</body>
</html>
```